Business Card Design

Kelvarspin

Industry/Entity Type

Business

Contact Information for Business Card

Marrowby Fields Lotto
Marrowby Fields Shopping Centre
Kiosk 3 No.47 Pelican Reach way
Harrowgate North
Dale Ostrowski
0413852276

```html
<!DOCTYPE html>
<html lang="en">
<head>
<meta charset="utf-8">
<title>Marrowby Fields Lotto – Business Card</title>
<link rel="stylesheet" href="https://fonts.googleapis.com/css2?family=Cinzel:wght@700&family=Arimo:wght@400&display=swap">
<style>
  :root {
    --page-bg: #e6e4e0;
    --card-red: #c8171d;
    --card-red-deep: #9c0f14;
    --card-cream: #f6f0dc;
    --ink-red: #b3141a;
    --ink-white: #ffffff;
  }
  html, body {
    margin: 0;
    width: 1200px;
    height: 863px;
    overflow: hidden;
    background: var(--page-bg);
  }
  .business-card {
    position: absolute;
    left: 150px;
    top: 174px;
    width: 900px;
    height: 514px;
    border-radius: 30px;
    overflow: hidden;
    background: var(--card-cream);
    box-shadow: 0 10px 30px rgba(0,0,0,0.18);
  }
  .card-shapes {
    position: absolute;
    inset: 0;
  }
  .brand {
    position: absolute;
    left: 46px;
    top: 62px;
    display: flex;
    align-items: center;
    gap: 14px;
    color: var(--ink-white);
  }
  .brand-dot {
    width: 38px;
    height: 38px;
    border-radius: 50%;
    background: var(--ink-white);
    flex: none;
  }
  .brand-name {
    font-family: "Cinzel", serif;
    font-weight: 700;
    font-size: 21px;
    letter-spacing: 0.5px;
    padding-bottom: 5px;
    border-bottom: 1px solid var(--ink-white);
  }
  .brand-tagline {
    font-family: "Arimo", sans-serif;
    font-size: 11.5px;
    margin-top: 4px;
  }
  .holder-name {
    position: absolute;
    left: 430px;
    top: 150px;
    width: 440px;
    margin: 0;
    font-family: "Cinzel", serif;
    font-weight: 700;
    font-size: 44px;
    line-height: 1;
    color: var(--ink-red);
    text-align: right;
  }
  .name-rule {
    position: absolute;
    left: 400px;
    top: 208px;
    width: 480px;
    height: 1.5px;
    background: var(--ink-red);
  }
  .contact {
    position: absolute;
    font-family: "Arimo", sans-serif;
    font-size: 19px;
    color: var(--ink-red);
    display: flex;
    align-items: center;
    gap: 8px;
  }
  .contact svg { fill: var(--ink-red); flex: none; }
  .contact-address { left: 408px; top: 220px; }
  .contact-phone { right: 30px; top: 258px; }
</style>
</head>
<body>
  <div class="business-card">
    <svg class="card-shapes" width="900" height="514" viewBox="0 0 900 514" aria-hidden="true">
      <defs>
        <linearGradient id="red-panel" x1="0" y1="0" x2="1" y2="0">
          <stop offset="0" stop-color="#b8141a"/>
          <stop offset="0.6" stop-color="#e0242a"/>
          <stop offset="1" stop-color="#c8171d"/>
        </linearGradient>
      </defs>
      <rect class="red-panel" x="0" y="0" width="600" height="345" fill="url(#red-panel)"/>
      <circle class="cream-disc" cx="630" cy="170" r="262" fill="var(--card-cream)"/>
      <path class="disc-edge" d="M 380 250 A 262 262 0 0 0 892 225" fill="none" stroke="var(--card-red-deep)" stroke-width="9"/>
    </svg>

    <div class="brand">
      <span class="brand-dot"></span>
      <div>
        <div class="brand-name">Marrowby Fields Lotto</div>
        <div class="brand-tagline">Marrowby Fields Shopping Centre Kiosk 3</div>
      </div>
    </div>

    <h1 class="holder-name">Dale Ostrowski</h1>
    <div class="name-rule"></div>

    <div class="contact contact-address">
      <svg width="14" height="18" viewBox="0 0 14 18"><path d="M7 0a7 7 0 0 0-7 7c0 5 7 11 7 11s7-6 7-11a7 7 0 0 0-7-7zm0 10a3 3 0 1 1 0-6 3 3 0 0 1 0 6z"/></svg>
      <span>No.47 Pelican Reach way Harrowgate North</span>
    </div>
    <div class="contact contact-phone">
      <svg width="12" height="20" viewBox="0 0 12 20"><path d="M2 0h8a2 2 0 0 1 2 2v16a2 2 0 0 1-2 2H2a2 2 0 0 1-2-2V2a2 2 0 0 1 2-2zm0 3v12h8V3z"/></svg>
      <span>041 385 2276</span>
    </div>
  </div>
</body>
</html>
```